Velmira Tork

I need a website designed to feature a new product for my company. I am dedicating a separate site just highlight the program. The url will be velmira2tork.com and the product name is velmira tork. The product is ringless voicemail. We take a recorded script and send it to our clients customers cell phones without the phone ringing.

The site will consist of a home page. I animated video demo. It will house 18 scripts and voice overs to match, a results page, and a page to request a live demo.

We sell the product to new car dealerships

```html
<!DOCTYPE html>
<html lang="en">
<head>
<meta charset="utf-8">
<title>Velmira Tork – Ringless Voicemail for Dealerships</title>
<link rel="stylesheet" href="https://fonts.googleapis.com/css2?family=Open+Sans:ital,wght@0,300;0,400;0,600;0,700;1,400&display=swap">
<style>
:root{
  --orange:#f47a20;
  --sky:#4ab3ec;
  --navy:#2353a0;
  --ink:#333333;
  --grey:#8a8f94;
  --pale:#f2f2f2;
  --line:#dcdfe3;
  --white:#ffffff;
  --tick:#2d8fd5;
}
*{box-sizing:border-box;margin:0;padding:0}
html,body{width:1200px;height:3455px;overflow:hidden}
body{font-family:"Open Sans",Arial,sans-serif;color:var(--ink);background:var(--white);position:relative}
section,header,footer{position:absolute;left:0;width:1200px}
.abs{position:absolute}

/* hero */
.hero{top:0;height:636px;background:linear-gradient(120deg,#6e5a3c 0%,#9a8a64 40%,#5f5a49 70%,#3f3a30 100%)}
.hero-photo{position:absolute;inset:0;background:radial-gradient(circle at 62% 45%,rgba(240,228,210,.55),rgba(0,0,0,0) 45%)}
.brand{left:143px;top:36px;font-size:30px;font-weight:600;color:var(--white);letter-spacing:.5px}
.nav{right:160px;top:40px;display:flex;align-items:center}
.nav a{color:var(--white);text-decoration:none;font-size:17px;padding:8px 15px;border-radius:22px}
.nav a.active{background:var(--sky);padding:8px 24px}
.hero-title{left:138px;top:228px;font-size:46px;font-weight:400;color:var(--white)}
.hero-sub{left:138px;top:290px;font-size:29px;line-height:44px;color:var(--white);font-weight:400}
.dots{left:143px;top:398px;display:flex;gap:8px}
.dots i{width:14px;height:14px;border-radius:50%;background:var(--white);display:block}
.dots i.off{background:transparent;border:2px solid var(--white)}

/* how it works */
.how{top:636px;height:621px;background:var(--pale)}
.section-title{width:100%;text-align:center;font-size:34px;font-weight:400;color:var(--ink)}
.how .section-title{top:54px}
.how .rule{top:78px;height:1px;background:#999;width:105px}
.step{width:210px;text-align:center}
.step .ring{width:114px;height:114px;margin:0 auto;border-radius:50%;border:2px solid var(--line);background:var(--white);position:relative;display:flex;align-items:center;justify-content:center}
.step .num{position:absolute;bottom:-14px;left:50%;transform:translateX(-50%);width:44px;height:28px;border-radius:14px;background:var(--sky);color:var(--white);font-size:17px;font-weight:600;line-height:28px}
.step p{margin-top:26px;font-size:13.5px;line-height:21px;color:#9a9ea3}

/* offer */
.offer{top:1257px;height:424px;background:var(--white)}
.phones{left:143px;top:49px;width:430px;height:375px;background:linear-gradient(180deg,#f4f5f7,#dfe2e6);border-radius:40px 40px 0 0}
.offer h2{left:613px;top:88px;font-size:29px;font-weight:600;color:var(--ink)}
.offer ul{left:613px;top:142px;width:440px;list-style:none}
.offer li{position:relative;padding-left:34px;font-size:14px;line-height:26px;color:#555;margin-bottom:6px}
.offer li svg{position:absolute;left:0;top:4px}

/* testimonial */
.quote{top:1681px;height:221px;background:var(--orange)}
.avatar{left:147px;top:48px;width:126px;height:126px;border-radius:50%;border:4px solid var(--white);background:linear-gradient(160deg,#c9b8a6,#7c6a5a)}
.quote .bar{left:302px;top:40px;width:2px;height:140px;background:rgba(255,255,255,.6)}
.quote blockquote{left:336px;top:56px;width:715px;font-style:italic;font-size:14.5px;line-height:27.5px;color:var(--white)}
.quote .mark{font-size:32px;line-height:0;font-style:normal}
.quote cite{left:336px;top:158px;font-style:normal;font-size:14.5px;font-weight:700;color:var(--white)}

/* video */
.video{top:1902px;height:486px}
.video-frame{left:359px;top:39px;width:475px;height:304px;border:6px solid var(--white);box-shadow:0 0 0 1px #ddd;background:linear-gradient(135deg,#3aa7e0,#2a8ed0)}
.play{left:50%;top:50%;transform:translate(-50%,-50%)}
.partners{left:131px;top:410px;width:951px;display:flex;justify-content:space-between;align-items:center}
.partners span{font-size:22px;font-weight:700;color:#3a3a3a}

/* scripts */
.scripts{top:2388px;height:417px;background:linear-gradient(90deg,var(--sky) 0%,#3a8ed7 45%,var(--navy) 100%)}
.scripts .section-title{top:56px;color:var(--white);font-weight:300;font-size:33px}
.col{width:300px}
.col.wide{width:360px}
.item{display:flex;align-items:center;gap:10px;height:44px;color:var(--white);font-size:14px}
.item svg{flex:0 0 28px}

/* contact */
.contact{top:2805px;height:449px;background:linear-gradient(180deg,#f3f3f1,#ebeae6)}
.subscribe{left:152px;top:35px;width:421px;height:362px;background:var(--orange);color:var(--white)}
.sub-mark{left:40px;top:30px;width:56px;height:56px;border-radius:50%;background:var(--white)}
.subscribe h3{position:absolute;left:118px;top:30px;font-size:20px;font-weight:600}
.subscribe .lead{position:absolute;left:118px;top:58px;width:270px;font-size:14px;line-height:22px}
.field{position:absolute;font-size:14px;border-bottom:1px solid rgba(255,255,255,.8);padding-bottom:10px}
.btn{position:absolute;left:40px;top:296px;width:110px;height:38px;background:var(--white);color:var(--orange);font-size:14px;font-weight:700;text-align:center;line-height:38px;border-radius:3px}
.privacy{position:absolute;left:172px;top:306px;font-size:13px}
.c-brand{left:613px;top:44px;font-size:31px;font-weight:600;color:var(--orange)}
.c-rule{left:613px;top:94px;width:120px;height:2px;background:var(--orange)}
.c-title{left:613px;top:122px;font-size:22px;font-weight:600;color:var(--ink)}
.c-text{left:613px;top:166px;width:520px;font-size:14px;line-height:22px;color:#444}
.c-row{left:613px;display:flex;align-items:center;gap:18px;font-size:18px;color:#333}
.c-ico{width:40px;height:40px;border-radius:50%;border:2px solid var(--orange);display:flex;align-items:center;justify-content:center}

/* footer */
.footer{top:3254px;height:201px;background:var(--white)}
.f-nav{top:42px;width:100%;display:flex;justify-content:center;gap:44px;font-size:15px;color:#444}
.copy{top:76px;width:100%;text-align:center;font-size:13px;color:#888}
.social{top:127px;width:100%;display:flex;justify-content:center;gap:9px}
.social i{display:block;width:28px;height:28px;border-radius:50%;background:var(--tick)}
.social i:last-child{background:#d34836}
</style>
</head>
<body>

<header class="hero">
  <div class="hero-photo" role="img" aria-label="Photograph of hands holding a smartphone showing the product app"></div>
  <div class="abs brand">velmira tork</div>
  <nav class="abs nav">
    <a class="active">Home</a><a>How It Works</a><a>Results</a><a>Contact Us</a><a>About Us</a><a>Blog</a>
  </nav>
  <h1 class="abs hero-title">Velmira Tork</h1>
  <p class="abs hero-sub">Fast, Effective, Inexpensive,<br>Versatile Marketing</p>
  <div class="abs dots"><i class="off"></i><i></i><i></i><i></i></div>
</header>

<section class="how">
  <h2 class="abs section-title">How it Works</h2>
  <div class="abs rule" style="left:440px"></div>
  <div class="abs rule" style="left:655px"></div>

  <div class="abs step" style="left:135px;top:134px">
    <div class="ring"><svg width="50" height="50" viewBox="0 0 50 50" fill="none" stroke="#2d7fd0" stroke-width="3"><rect x="8" y="6" width="34" height="38" rx="3"/><path d="M15 16h3M23 16h12M15 25h3M23 25h12M15 34h3M23 34h12"/></svg><span class="num">1</span></div>
    <p>We select a trageted list of past sales customers, service customers, or un sold leads</p>
  </div>
  <div class="abs step" style="left:367px;top:134px">
    <div class="ring"><svg width="50" height="50" viewBox="0 0 50 50" fill="none" stroke="#2d7fd0" stroke-width="4" stroke-linecap="round"><path d="M10 40L34 16M30 8l12 12M12 10l28 30"/></svg><span class="num">2</span></div>
    <p>We develop and record a script based on your stores current needs, incentives, time of year, and list</p>
  </div>
  <div class="abs step" style="left:620px;top:134px">
    <div class="ring"><svg width="54" height="50" viewBox="0 0 54 50" fill="#2d7fd0"><circle cx="27" cy="15" r="8"/><circle cx="12" cy="19" r="6"/><circle cx="42" cy="19" r="6"/><path d="M14 42c0-10 6-16 13-16s13 6 13 16z"/><path d="M2 40c0-8 4-12 10-12 3 0 5 1 6 2-3 3-4 6-4 10z"/><path d="M52 40c0-8-4-12-10-12-3 0-5 1-6 2 3 3 4 6 4 10z"/></svg><span class="num">3</span></div>
    <p>Your team will be coached and given a set of scripted responsive to be sure everyone is prepared</p>
  </div>
  <div class="abs step" style="left:855px;top:134px">
    <div class="ring"><svg width="50" height="50" viewBox="0 0 50 50" fill="#2d7fd0"><path d="M42 8c-12 0-20 8-24 16l8 8c8-4 16-12 16-24z"/><path d="M16 26l-8 2 6-10h8zM24 34l-2 8 10-6v-8zM14 34l-6 8 8-6z"/></svg><span class="num">4</span></div>
    <p>Your message and list are uploaded to our system and delivered at any speed you</p>
  </div>

  <div class="abs step" style="left:135px;top:372px">
    <div class="ring"><svg width="44" height="44" viewBox="0 0 24 24" fill="#2d7fd0"><path d="M6.6 10.8a15.1 15.1 0 0 0 6.6 6.6l2.2-2.2c.3-.3.7-.4 1-.2 1.1.4 2.3.6 3.6.6.6 0 1 .4 1 1V20c0 .6-.4 1-1 1A17 17 0 0 1 3 4c0-.6.4-1 1-1h3.5c.6 0 1 .4 1 1 0 1.3.2 2.5.6 3.6.1.3 0 .7-.2 1z"/></svg><span class="num">5</span></div>
    <p>Inbound return calls will begin within minutes</p>
  </div>
  <div class="abs step" style="left:367px;top:372px">
    <div class="ring"><svg width="50" height="50" viewBox="0 0 50 50"><circle cx="25" cy="25" r="15" fill="none" stroke="#2d7fd0" stroke-width="8" stroke-dasharray="6 4"/><circle cx="25" cy="25" r="11" fill="#2d7fd0"/><circle cx="25" cy="25" r="5" fill="#fff"/></svg><span class="num">6</span></div>
    <p>This program required<br>zero set up</p>
  </div>
  <div class="abs step" style="left:620px;top:372px">
    <div class="ring"><svg width="46" height="46" viewBox="0 0 46 46" fill="none" stroke="#2d7fd0" stroke-width="4" stroke-linecap="round"><circle cx="23" cy="23" r="18"/><path d="M23 12v11h8"/></svg><span class="num">7</span></div>
    <p>The simple process above can be completed and go live in as little as 24 hours.</p>
  </div>
  <div class="abs step" style="left:855px;top:372px">
    <div class="ring"><svg width="40" height="50" viewBox="0 0 40 50" fill="none" stroke="#2d7fd0" stroke-width="3.5" stroke-linecap="round"><rect x="13" y="4" width="14" height="26" rx="7"/><path d="M6 22c0 8 6 14 14 14s14-6 14-14M20 36v8M12 46h16"/></svg><span class="num">8</span></div>
    <p>Every inbound phone call is recorded, tracked, and caller id information</p>
  </div>
</section>

<section class="offer">
  <div class="abs phones" role="img" aria-label="Two smartphones showing a voicemail inbox and a sample dealership script"></div>
  <h2 class="abs">THE OFFER</h2>
  <ul class="abs">
    <li><svg width="18" height="18" viewBox="0 0 18 18"><circle cx="9" cy="9" r="9" fill="#2d8fd5"/><path d="M5 9l3 3 5-6" stroke="#fff" stroke-width="2" fill="none"/></svg>We can use this as a buy back offer, re-engage unsold CRM leads, offer monthly factory incentives, inform of a sales event, or to get CSI surveys completed</li>
    <li><svg width="18" height="18" viewBox="0 0 18 18"><circle cx="9" cy="9" r="9" fill="#2d8fd5"/><path d="M5 9l3 3 5-6" stroke="#fff" stroke-width="2" fill="none"/></svg>It can be recorded by anyone!</li>
    <li><svg width="18" height="18" viewBox="0 0 18 18"><circle cx="9" cy="9" r="9" fill="#2d8fd5"/><path d="M5 9l3 3 5-6" stroke="#fff" stroke-width="2" fill="none"/></svg>Works because the message is perfect every time!</li>
    <li><svg width="18" height="18" viewBox="0 0 18 18"><circle cx="9" cy="9" r="9" fill="#2d8fd5"/><path d="M5 9l3 3 5-6" stroke="#fff" stroke-width="2" fill="none"/></svg>The information stays with them!</li>
  </ul>
</section>

<section class="quote">
  <div class="abs avatar" role="img" aria-label="Portrait photo of the dealer giving the testimonial"></div>
  <div class="abs bar"></div>
  <blockquote class="abs"><span class="mark">“</span> I have used Velmira Tork to my sales and service database as well as to unsold leads. I have been surprised that the results are as advertised. We get a steady stream of traffic from these messages and I have incorporated this program into all of my stores monthly budgets <span class="mark">”</span></blockquote>
  <cite class="abs">DORIAN P LAKEVIEW NORVANE DEALER</cite>
</section>

<section class="video">
  <div class="abs video-frame" role="img" aria-label="Animated video demo illustration of voicemail messages flying from a phone">
    <svg class="abs play" width="60" height="60" viewBox="0 0 60 60"><circle cx="30" cy="30" r="28" fill="rgba(0,0,0,.35)" stroke="#fff" stroke-width="2"/><path d="M24 18l18 12-18 12z" fill="#fff"/></svg>
  </div>
  <div class="abs partners">
    <span>Norvane</span><span>Belcrest</span><span>Garrow</span><span>Fenwick</span><span>Jastro</span><span>Rulo</span><span>Delmar</span><span>Corvex</span>
  </div>
</section>

<section class="scripts">
  <h2 class="abs section-title">Available Scripts</h2>
  <div class="abs col" style="left:161px;top:144px">
    <div class="item"><svg width="28" height="28" viewBox="0 0 30 30" stroke="#fff" stroke-width="2" fill="none"><path d="M15 3v24M4 9l22 12M4 21l22-12"/></svg>January- New Years</div>
    <div class="item"><svg width="28" height="28" viewBox="0 0 30 30" stroke="#fff" stroke-width="2" fill="none"><path d="M15 2v26M3 15h24M6 6l18 18M24 6L6 24"/></svg>February- Winter Special</div>
    <div class="item"><svg width="28" height="28" viewBox="0 0 30 30" fill="#fff"><circle cx="15" cy="13" r="9"/><rect x="12" y="22" width="6" height="5"/></svg>March- Spring Forward</div>
    <div class="item"><svg width="28" height="28" viewBox="0 0 30 30" fill="#fff"><circle cx="15" cy="17" r="10"/><rect x="11" y="3" width="8" height="5"/></svg>April- Tax Time</div>
  </div>
  <div class="abs col" style="left:433px;top:144px">
    <div class="item"><svg width="28" height="28" viewBox="0 0 30 30" fill="#fff"><path d="M4 4h22v5H4zM6 9h18l-3 18H9z"/></svg>May- Memorial Day</div>
    <div class="item"><svg width="28" height="28" viewBox="0 0 30 30" fill="#fff"><path d="M3 22c6-4 18-4 24 0v4H3zM15 4l8 14H7z"/></svg>June- Summer Saving</div>
    <div class="item"><svg width="28" height="28" viewBox="0 0 30 30" fill="#fff"><path d="M4 14l10-8 12 4-6 4 4 10-10-6-6 4z"/></svg>July- Independence Day</div>
    <div class="item" style="line-height:18px"><svg width="28" height="28" viewBox="0 0 30 30" fill="#fff"><path d="M3 10L15 4l12 6-12 6zM8 14v8h14v-8l-7 4z"/></svg>August- Back To School/Model<br>Year End</div>
  </div>
  <div class="abs col wide" style="left:737px;top:144px">
    <div class="item"><svg width="28" height="28" viewBox="0 0 30 30" fill="#fff"><path d="M4 26L20 10l6 6-16 16zM18 4l8 8-3 3-8-8z"/></svg>September- Labor Day</div>
    <div class="item"><svg width="28" height="28" viewBox="0 0 30 30" fill="#fff"><path d="M15 3l4 8 8 1-6 6 2 9-8-5-8 5 2-9-6-6 8-1z"/></svg>October- Fall Into Savings</div>
    <div class="item"><svg width="28" height="28" viewBox="0 0 30 30" fill="#fff"><path d="M4 13h6v14H4zM12 27h11l3-12h-9l2-8c0-3-4-3-4 0l-3 7z"/></svg>November- Giving Thanks/Black Friday</div>
    <div class="item"><svg width="28" height="28" viewBox="0 0 30 30" fill="#fff"><path d="M3 16a12 12 0 0 1 24 0zM14 16h2v9a3 3 0 0 1-6 0h2a1 1 0 0 0 2 0z"/></svg>December- Happy Holidays/Year End</div>
  </div>
</section>

<section class="contact" role="img" aria-label="Faint street map background">
  <div class="abs subscribe">
    <div class="abs sub-mark"></div>
    <h3>SUBSCRIBE</h3>
    <p class="lead">Sign up with your email address to receive the latest news and updates.</p>
    <div class="field" style="left:40px;top:126px;width:340px">First Name</div>
    <div class="field" style="left:40px;top:172px;width:340px">Last Name</div>
    <div class="field" style="left:40px;top:220px;width:340px">Email Address</div>
    <div class="field" style="left:40px;top:266px;width:160px">Dealership name</div>
    <div class="field" style="left:215px;top:266px;width:165px">Phone Number</div>
    <div class="btn" style="top:310px">SIGN UP</div>
    <div class="privacy" style="top:320px">We respect your privacy.</div>
  </div>
  <div class="abs c-brand">velmira tork</div>
  <div class="abs c-rule"></div>
  <div class="abs c-title">Got a question or comment?</div>
  <p class="abs c-text">We are constantly working to raise the bar on our services. If you have any questions or concerns about your experience, please let us know.</p>
  <div class="abs c-row" style="top:238px"><span class="c-ico"><svg width="18" height="14" viewBox="0 0 18 14"><rect width="18" height="14" rx="2" fill="#f47a20"/><path d="M1 2l8 6 8-6" stroke="#fff" stroke-width="1.5" fill="none"/></svg></span>Mail Us At: info@halvoremarketing.com</div>
  <div class="abs c-row" style="top:293px"><span class="c-ico"><svg width="18" height="18" viewBox="0 0 24 24" fill="#f47a20"><path d="M6.6 10.8a15.1 15.1 0 0 0 6.6 6.6l2.2-2.2c.3-.3.7-.4 1-.2 1.1.4 2.3.6 3.6.6.6 0 1 .4 1 1V20c0 .6-.4 1-1 1A17 17 0 0 1 3 4c0-.6.4-1 1-1h3.5c.6 0 1 .4 1 1 0 1.3.2 2.5.6 3.6.1.3 0 .7-.2 1z"/></svg></span>Call Us At: 303 555 0147</div>
</section>

<footer class="footer">
  <nav class="abs f-nav"><span>Home</span><span>How It Works</span><span>Results</span><span>Contact Us</span><span>About Us</span><span>Blog</span></nav>
  <p class="abs copy">© 2016 Company Name. All right reserved. Term of Use</p>
  <div class="abs social"><i></i><i></i><i></i><i></i></div>
</footer>

</body>
</html>
```